Awesome business card design needed

We need a new business card design to go with our new logo.
We are a web development agency that specialises in highly complex back-end integrations as opposed to design, our customers are retailers, hotels, hospitals and any other organisation that has a large online marketing department.
Take a look at our website - www.orvekplus.com for some inspiration.
We want our new business cards to exude class, professionalism and style.
We are likely to choose a high-end card to print them on but we want the design of the card itself to really turn heads.
We have no specific colour requirements, the logo as you will see is a turquoise colour R89 G171 B167 #59aba7 but it can also be in white if you want to make the colour of the card something different.
The information on the card should be:
Name
Position
Tel
email
Potentially a double sided card could have our web address, twitter and FB links.

```html
<!DOCTYPE html>
<html lang="en">
<head>
<meta charset="utf-8">
<title>Orvekplus Business Card</title>
<link rel="stylesheet" href="https://fonts.googleapis.com/css2?family=Michroma&display=swap">
<style>
  :root {
    --stage: #2b2b2b;
    --turquoise: #59aba7;
    --ink: #0b0b0b;
    --card-black: #121212;
  }
  * { box-sizing: border-box; margin: 0; padding: 0; }
  html, body { width: 1200px; height: 900px; overflow: hidden; }
  body {
    background: var(--stage);
    font-family: "Michroma", sans-serif;
    position: relative;
  }
  .card {
    position: absolute;
    top: 300px;
    width: 530px;
    height: 300px;
    border-radius: 2px;
    overflow: hidden;
  }
  .card-front { left: 45px; background: var(--card-black); }
  .card-back { left: 625px; background: var(--turquoise); }

  .front-pattern {
    position: absolute; inset: 0;
    background: linear-gradient(135deg, #161616, #0e0e0e);
  }
  .front-wordmark {
    position: absolute; left: 0; right: 0; top: 50%;
    transform: translateY(-50%);
    text-align: center;
    color: var(--turquoise);
    font-size: 58px;
    letter-spacing: 2px;
  }

  .name-tag {
    position: absolute; left: 0; top: 92px;
    width: 220px; height: 52px;
    background: var(--ink);
    border-radius: 0 8px 8px 0;
    padding: 8px 0 0 24px;
    color: var(--turquoise);
  }
  .name-tag .person-name { font-size: 12.5px; letter-spacing: 0.5px; text-transform: uppercase; }
  .name-tag .person-role { font-size: 9px; margin-top: 4px; }

  .back-wordmark {
    position: absolute; right: 36px; top: 80px;
    color: var(--ink);
    font-size: 36px;
    letter-spacing: 1px;
  }

  .contact-list {
    position: absolute; right: 30px; top: 178px;
    list-style: none;
    color: var(--ink);
    font-size: 11px;
    text-align: right;
  }
  .contact-list li {
    display: flex; align-items: center; justify-content: flex-end;
    gap: 8px; height: 21px;
  }
  .contact-list .phone-line { font-size: 12px; }
  .contact-icon { width: 17px; height: 17px; flex: none; }
</style>
</head>
<body>
  <section class="card card-front">
    <div class="front-pattern" role="img" aria-label="Dark checkered pixel pattern background"></div>
    <div class="front-wordmark">orvekplus</div>
  </section>

  <section class="card card-back">
    <div class="name-tag">
      <div class="person-name">Talia Renwick</div>
      <div class="person-role">Customer Service</div>
    </div>

    <div class="back-wordmark">orvekplus</div>

    <ul class="contact-list">
      <li class="phone-line">555.014.2287
        <svg class="contact-icon" viewBox="0 0 20 20"><circle cx="10" cy="10" r="8.5" fill="none" stroke="#0b0b0b" stroke-width="1.3"/><path d="M8 5.5c-1.5 1-1.6 3.4 0 6s3.6 3.8 5 3l-1.3-2-1.3.6c-.8-.6-1.6-1.9-1.9-3l1.1-.8z" fill="#0b0b0b"/></svg>
      </li>
      <li>talia@orvekplus.com
        <svg class="contact-icon" viewBox="0 0 20 20"><circle cx="10" cy="10" r="8.5" fill="none" stroke="#0b0b0b" stroke-width="1.3"/><rect x="5.5" y="7" width="9" height="6.5" fill="#0b0b0b"/><path d="M5.5 7l4.5 3.5L14.5 7" fill="none" stroke="#59aba7" stroke-width="0.9"/></svg>
      </li>
      <li>www.orvekplus.com
        <svg class="contact-icon" viewBox="0 0 20 20"><circle cx="10" cy="10" r="8.5" fill="none" stroke="#0b0b0b" stroke-width="1.3"/><circle cx="10" cy="10" r="4" fill="none" stroke="#0b0b0b" stroke-width="1.2"/><path d="M6 10h8M10 6v8" stroke="#0b0b0b" stroke-width="0.9"/></svg>
      </li>
      <li>feed.orvekplus.com
        <svg class="contact-icon" viewBox="0 0 20 20"><circle cx="10" cy="10" r="8.5" fill="none" stroke="#0b0b0b" stroke-width="1.3"/></svg>
      </li>
      <li>@orvekplus
        <svg class="contact-icon" viewBox="0 0 20 20"><circle cx="10" cy="10" r="8.5" fill="none" stroke="#0b0b0b" stroke-width="1.3"/></svg>
      </li>
    </ul>
  </section>
</body>
</html>
```